サイト構成・基本的な要件については
https://zubalo.com/boards/kQpTrnVxaYeL42dm
を併せてご覧いただければ幸いです。

また、店舗写真・ロゴについては
http://nuvadrop.jp/get/7a1be93c50df28e47a6b0c13f8d52e9a61f7b0de
よりダウンロードいただければと存じます。

上記だけで制作が難しい場合は
http://molvu.jp/
http://jp.grenaxi.com/
http://www.plimbrook.com/ja/cat-27-Beauty-Fashion.html
などから、10000円程度までならこちらにて購入可能です。
カンプデータにて作成頂き、
納品時に当方にて購入したデータに差し替えていただければと存じます。

ページ構成もシンプルですので
TOPページからすべての導線を配置するかたちでデザインいただければと存じます。
当方、jqueryなどのコーディングも対応可能ですので、
そういったデザイン提案を頂いても大丈夫です。

色合いは、店舗に合わせた、シンプルで明るい色合いを希望いたします。
木目、ブラウンを採用しているので、
そちらを展開した形のカラーパターンが合うかなと考えていますが、
特に絶対的な指定はありません。
http://beauty.tarukami.jp/slnQ000583716/
1ページ
茶系、店舗のイメージを展開するような色合いですと幸いです。
• 高解像度JPG (.jpg)
• フォトショップ形式 (.psd)
サイト構成・基本的な要件については
を併せてご覧いただければ幸いです。

また、写真・素材については
よりダウンロードいただければと存じます。

上記だけで制作が難しい場合は
http://molvu.jp/
http://jp.grenaxi.com/
などから、10000円程度までならこちらにて購入可能です。カンプデータにて作成頂き、納品時に当方にて購入したデータに差し替えていただければと存じます。

基本的には、大きなイメージ写真を前面に出して訴求しつつ
明るいイメージでまとめられればと思います。

【参考イメージ】
http://senbarusika.jp/ (色合い、明るい印象)
http://www.mabeku.jp/home/studydesk/product/vozlan/(色合い、明るい印象)

余りかしこまった雰囲気にしてしまうよりは、柔らかく明るい印象にすることで、男女とも入りやすいサロンということをアピールできればと考えています。
制作につきましてご不明な点がございましたら、
お気軽にお申し付けいただければと存じます。
ご提案お待ちしております
ご質問にて、ワイヤーフレーム提示のご要望がありましたので追記いたします。

https://zubalo.com/boards/pHnRtc7XmW9vqdz5

上記が、当方で想定しているワイヤーですが、
あまり上記にこだわらず、ご提案頂ければ幸甚です。
ご不明な点がございましたらお気軽にお申し付けください。
http://nuvadrop.jp/get/82ce5d0a93bf714e6c2d08a1f5b937e40d6ac5b1

念のため、素材を再アップいたします。

クライアントとの協議の結果、こちらの案を採用させていただきました。
スタイリッシュなデザインとサイト全体の見やすさ、信頼感、
文字などの読みやすさが大変気に入り、
そちらが採用の決め手となりました。

この度は多数ご提案いただきありがとうございました。
当選に至らなかったランサー様におかれましては大変心苦しいのですが、
次の機会にぜひご提案いただければ幸甚です。
引き続き何卒よろしくお願いいたします。

```html
<!DOCTYPE html>
<html lang="ja">
<head>
<meta charset="utf-8">
<title>CUT STUDIO BREEZE</title>
<link href="https://fonts.googleapis.com/css2?family=Noto+Sans+JP:wght@400;700&family=Noto+Serif+JP:wght@500;700&display=swap" rel="stylesheet">
<style>
:root{
  --bg:#f3f1ee;
  --paper:#ffffff;
  --brown:#4a3a2c;
  --brown-dark:#3a2d22;
  --tan:#e7ddd0;
  --tan-deep:#cdb89c;
  --orange:#e8743b;
  --text:#4d4640;
  --muted:#8a8178;
  --line:#ddd6cd;
}
*{box-sizing:border-box;margin:0;padding:0}
html,body{width:1200px;height:2748px;overflow:hidden}
body{background:var(--bg);font-family:"Noto Sans JP",sans-serif;color:var(--text);position:relative}
.hero{position:absolute;left:0;top:0;width:1200px;height:520px;background:linear-gradient(120deg,#d9c7ae 0%,#efe5d6 45%,#c9b090 75%,#8c6a48 100%)}
.hero-logo{position:absolute;left:0;top:40px;width:1200px;height:100px;display:flex;align-items:center;justify-content:center;gap:12px;font-family:"Noto Serif JP",serif;font-weight:700;font-size:24px;color:var(--brown);letter-spacing:2px;white-space:nowrap}
.hero-logo i{width:14px;height:14px;background:var(--brown);display:block}
.hero-copy{position:absolute;right:120px;top:268px;text-align:right;font-family:"Noto Serif JP",serif;font-weight:500;font-size:22px;line-height:44px;color:#fff;text-shadow:0 1px 4px rgba(60,40,20,.6)}
.nav{position:absolute;top:520px;left:0;width:1200px;height:120px;background:var(--paper);border-bottom:1px solid var(--line)}
.nav ul{list-style:none;display:flex;position:absolute;left:80px;top:35px;height:50px}
.nav li{width:142px;text-align:center;font-size:14px;line-height:50px;border-right:1px solid var(--line);color:var(--brown);white-space:nowrap}
.nav li:first-child{border-left:1px solid var(--line)}
.nav .reserve{position:absolute;left:970px;top:32px;width:150px;height:56px;background:var(--orange);color:#fff;font-size:15px;text-align:center;line-height:56px;border-radius:4px;font-weight:700;white-space:nowrap}
.welcome{position:absolute;left:240px;top:720px;width:720px}
.sec-title{font-family:"Noto Serif JP",serif;font-weight:700;font-size:30px;color:var(--brown);display:flex;align-items:center;gap:10px;white-space:nowrap}
.sec-title svg{flex:none}
.welcome p{position:absolute;top:80px;left:0;width:420px;font-size:14px;line-height:28px}
.welcome-photo{position:absolute;left:450px;top:72px;width:270px;height:300px;background:linear-gradient(160deg,#6b5240,#2e241c)}
.tiles{position:absolute;left:240px;top:1140px;width:720px;height:200px;background:var(--tan);display:flex;gap:16px;padding:20px}
.tile{flex:1;display:flex;flex-direction:column}
.tile .ph{height:124px;background:linear-gradient(150deg,#a58766,#5d4633)}
.tile span{margin-top:10px;text-align:center;font-size:14px;color:var(--brown);white-space:nowrap}
.contact{position:absolute;left:240px;top:1400px;width:720px;height:120px;display:flex;gap:20px}
.tel-box{flex:1;background:var(--paper);border:1px solid var(--line);display:flex;align-items:center;padding:0 20px;gap:18px}
.badge{width:74px;height:74px;border-radius:50%;background:var(--orange);color:#fff;font-size:13px;font-weight:700;display:flex;align-items:center;justify-content:center;text-align:center;line-height:18px;flex:none}
.tel-box strong{display:block;font-family:"Noto Serif JP",serif;font-size:30px;color:var(--brown);white-space:nowrap}
.tel-box small{font-size:11px;color:var(--muted);line-height:17px;display:block;white-space:nowrap}
.recruit{flex:1;background:linear-gradient(90deg,#f4ebdd,#d9c2a2);border:1px solid var(--line);padding:26px 30px}
.recruit em{font-style:normal;font-size:13px;color:var(--orange)}
.recruit b{display:block;font-family:"Noto Serif JP",serif;font-size:26px;color:var(--brown);margin-top:6px;white-space:nowrap}
.news{position:absolute;left:240px;top:1580px;width:720px}
.news .sec-title small{font-size:13px;color:var(--muted);font-family:"Noto Sans JP",sans-serif;font-weight:400;margin-left:6px}
.news ul{list-style:none;margin-top:20px}
.news li{display:flex;gap:30px;font-size:14px;padding:18px 20px;border-bottom:1px dotted var(--tan-deep);white-space:nowrap}
.news time{color:var(--orange)}
.map{position:absolute;left:0;top:1920px;width:1200px;height:440px;background:linear-gradient(135deg,#e9e6df,#dcd8cf 60%,#cfd9e3)}
.footer{position:absolute;left:0;top:2360px;width:1200px;height:388px;background:var(--brown)}
.pagetop{position:absolute;right:100px;top:-36px;width:120px;height:36px;background:var(--brown-dark);color:#fff;font-size:12px;text-align:center;line-height:36px}
.f-logo{position:absolute;left:240px;top:40px;display:flex;gap:10px;align-items:center;font-family:"Noto Serif JP",serif;font-weight:700;font-size:22px;color:#fff;letter-spacing:2px;white-space:nowrap}
.f-logo i{width:12px;height:12px;background:#fff;display:block}
.f-links{position:absolute;left:240px;top:130px;width:400px;font-size:12px;line-height:30px;color:#e8dccd;white-space:nowrap}
.f-info{position:absolute;left:660px;top:90px;color:#fff}
.f-info strong{font-family:"Noto Serif JP",serif;font-size:34px;display:block}
.f-info small{font-size:12px;line-height:22px;color:#e8dccd;display:block;white-space:nowrap}
.copy{position:absolute;left:0;bottom:0;width:1200px;height:50px;background:var(--brown-dark);color:#b9a893;font-size:11px;text-align:center;line-height:50px}
</style>
</head>
<body>
<header class="hero" role="img" aria-label="サロン店内、理容椅子と鏡のある明るい空間の写真">
  <div class="hero-logo"><i></i>CUT STUDIO BREEZE</div>
  <p class="hero-copy">スタイリスト全員が理容・美容両方の免許保持者<br>「美容院に行きたいけど照れがある」<br>そんな方のためのカットスタジオです</p>
</header>
<nav class="nav">
  <ul><li>サロン案内</li><li>メニュー・料金</li><li>シャンプーについて</li><li>スタッフ紹介</li><li>よくある質問</li><li>ギャラリー</li></ul>
  <div class="reserve">ご予約について</div>
</nav>
<section class="welcome">
  <h2 class="sec-title"><svg width="26" height="26" viewBox="0 0 26 26"><circle cx="6" cy="20" r="4" fill="none" stroke="#4a3a2c" stroke-width="2"/><circle cx="20" cy="20" r="4" fill="none" stroke="#4a3a2c" stroke-width="2"/><path d="M8 17L21 2M18 17L5 2" stroke="#4a3a2c" stroke-width="2"/></svg>CUT STUDIO BREEZEへようこそ</h2>
  <p>スタイリスト全員が理容・美容両方の免許保持者。「美容院に行きたいけど照れがある」そんな方のためのカットスタジオです。<br><br>このたびはCUT STUDIO BREEZEのホームページをご覧いただきありがとうございます。当店は、スタイリスト全員が理容・美容両方の資格を保有。男性の方も女性の方もお気軽にご来店いただける明るいサロンです。カットのプロとして丁寧なカウンセリングを心がけております。ご予約の上ぜひ一度ご来店ください。</p>
  <div class="welcome-photo" role="img" aria-label="店舗外観、看板のある入口の写真"></div>
</section>
<section class="tiles">
  <div class="tile"><div class="ph" role="img" aria-label="店内の写真"></div><span>サロン案内</span></div>
  <div class="tile"><div class="ph" role="img" aria-label="施術スペースの写真"></div><span>メニュー・料金</span></div>
  <div class="tile"><div class="ph" role="img" aria-label="シャンプーボトルの写真"></div><span>シャンプーについて</span></div>
  <div class="tile"><div class="ph" role="img" aria-label="スタッフの写真"></div><span>スタッフ紹介</span></div>
</section>
<section class="contact">
  <div class="tel-box"><div class="badge">ご予約は<br>こちら</div><div><strong>045-712-3398</strong><small>平日 9:00〜20:00 ／ 土日祝 9:00〜19:00<br>毎週火曜日、第3月曜定休</small></div></div>
  <div class="recruit"><em>Recruit</em><b>スタイリスト募集中</b></div>
</section>
<section class="news">
  <h2 class="sec-title"><svg width="22" height="22" viewBox="0 0 22 22"><path d="M3 3h12l4 4v12H3z" fill="none" stroke="#4a3a2c" stroke-width="2"/></svg>NEWS<small>最新情報</small></h2>
  <ul>
    <li><time>2016年03月02日</time>春の新メニューのご案内を掲載しました。ぜひご覧ください。</li>
    <li><time>2016年03月01日</time>3月の定休日と営業時間の変更についてお知らせします。</li>
    <li><time>2016年02月20日</time>ホームページをリニューアルオープンいたしました。</li>
  </ul>
</section>
<div class="map" role="img" aria-label="店舗周辺の地図"></div>
<footer class="footer">
  <div class="pagetop">▲ Page Top</div>
  <div class="f-logo"><i></i>CUT STUDIO BREEZE</div>
  <div class="f-links">サロン案内 ｜ メニュー・料金 ｜ シャンプーについて ｜ スタッフ紹介<br>よくある質問 ｜ ギャラリー ｜ ご予約について<br>プライバシーポリシー ｜ サイトマップ ｜ お問い合わせ</div>
  <div class="f-info"><strong>045-712-3398</strong><small>平日 9:00〜20:00 ／ 土日祝 9:00〜19:00　毎週火曜日、第3月曜定休</small><small>神奈川県横浜市緑風区青葉町3-18　青葉駅より徒歩5分</small></div>
  <div class="copy">COPYRIGHT © CUT STUDIO BREEZE ALL RIGHTS RESERVED.</div>
</footer>
</body>
</html>
```